VelaCure Wellness Business Cards

I am looking to have luxury business cards made for my IV Therapy and Wellness business.
Updates

Target Market(s)

Health and Wellness professionals

Industry/Entity Type

MedSpa

Contact Information for Business Card

Tobin Haverly, MSN, RN, CCRN Tobin@velacurewellness.com (916) 582-3179 QR code to website www.velacurewellness.com

```html
<!DOCTYPE html>
<html lang="en">
<head>
<meta charset="utf-8">
<title>VelaCure Wellness Business Cards</title>
<link href="https://fonts.googleapis.com/css2?family=Lato:wght@400;700;900&display=swap" rel="stylesheet">
<style>
  :root {
    --backdrop: #1e2526;
    --card: #2a2a2b;
    --brand-blue: #1b9ad6;
    --ink-light: #f2f2f2;
    --rule: #8a8a8a;
  }
  * { box-sizing: border-box; margin: 0; padding: 0; }
  html, body {
    width: 1200px;
    height: 880px;
    overflow: hidden;
    background: var(--backdrop);
    font-family: "Lato", sans-serif;
  }
  .canvas { position: relative; width: 1200px; height: 880px; }
  .card {
    position: absolute;
    width: 540px;
    height: 310px;
    background: var(--card);
    border-radius: 16px;
  }
  .card--front { left: 70px; top: 110px; }
  .card--back { left: 590px; top: 460px; }

  .wordmark {
    font-family: "Lato", sans-serif;
    font-weight: 400;
    letter-spacing: 0.5px;
    line-height: 1.05;
    display: flex;
    align-items: center;
    gap: 14px;
  }
  .wordmark__dot { border-radius: 50%; flex: none; }

  .card--front .wordmark {
    position: absolute; inset: 0;
    justify-content: center;
    color: var(--brand-blue);
    font-size: 48px;
  }
  .card--front .wordmark__dot { background: var(--brand-blue); width: 30px; height: 30px; }

  .card--back .wordmark {
    position: absolute;
    left: 0; top: 0; width: 290px; height: 310px;
    justify-content: center;
    color: var(--ink-light);
    font-size: 32px;
  }
  .card--back .wordmark__dot { background: var(--ink-light); width: 20px; height: 20px; }

  .divider {
    position: absolute;
    left: 290px; top: 78px;
    width: 1px; height: 154px;
    background: var(--rule);
  }
  .contact {
    position: absolute;
    left: 314px; top: 64px;
    color: var(--ink-light);
  }
  .contact__name {
    font-weight: 900;
    font-size: 24px;
    letter-spacing: 0.5px;
    line-height: 1.1;
  }
  .contact__title {
    font-size: 13px;
    margin-bottom: 12px;
  }
  .contact__list { list-style: none; font-size: 13px; line-height: 1.45; }
  .contact__item { display: flex; align-items: flex-start; gap: 9px; }
  .contact__icon { width: 11px; height: 11px; flex: none; margin-top: 4px; fill: var(--ink-light); }
</style>
</head>
<body>
<main class="canvas">
  <section class="card card--front" aria-label="Card front">
    <div class="wordmark"><span class="wordmark__dot"></span><span>VelaCure<br>Wellness</span></div>
  </section>

  <section class="card card--back" aria-label="Card back">
    <div class="wordmark"><span class="wordmark__dot"></span><span>VelaCure<br>Wellness</span></div>
    <div class="divider"></div>
    <div class="contact">
      <p class="contact__name">FULL NAME</p>
      <p class="contact__title">Profession/Title</p>
      <ul class="contact__list">
        <li class="contact__item">
          <svg class="contact__icon" viewBox="0 0 10 10"><path d="M5 0a3.5 3.5 0 0 0-3.5 3.5C1.5 6 5 10 5 10s3.5-4 3.5-6.5A3.5 3.5 0 0 0 5 0zm0 5a1.5 1.5 0 1 1 0-3 1.5 1.5 0 0 1 0 3z"/></svg>
          <span>PO Box 12345<br>State, Country, USA</span>
        </li>
        <li class="contact__item">
          <svg class="contact__icon" viewBox="0 0 10 10"><path d="M2 0l2 2.5-1 1.2c.6 1.3 1.6 2.3 2.8 2.9l1.2-1L9.5 7.5 8.2 9.6C4 9.2.8 6 .4 1.8z"/></svg>
          <span>123.456.7890</span>
        </li>
        <li class="contact__item">
          <svg class="contact__icon" viewBox="0 0 10 10"><path d="M2.5 0h5v10h-5zM3.3 1v7h3.4V1z"/></svg>
          <span>123.456.7890</span>
        </li>
        <li class="contact__item">
          <svg class="contact__icon" viewBox="0 0 10 10"><path d="M0 2h10v6H0zM0 2l5 3.5L10 2" stroke="#2a2a2b" stroke-width="0.8"/></svg>
          <span>info@youremail.com</span>
        </li>
        <li class="contact__item">
          <svg class="contact__icon" viewBox="0 0 10 10"><circle cx="5" cy="5" r="4.5"/><path d="M0.5 5h9M5 0.5c-2 2.5-2 6.5 0 9M5 0.5c2 2.5 2 6.5 0 9" stroke="#2a2a2b" stroke-width="0.7" fill="none"/></svg>
          <span>yourwebsite.com</span>
        </li>
      </ul>
    </div>
  </section>
</main>
</body>
</html>
```